Start-up Cleaning Business Needs Professional Business Cards

Marisol's Butler Tidying, LLC, is a start-up business based in the Northern Virginia suburbs of Washington, DC. MBT provides cleaning and housekeeping services for homes and offices. We have three core values:

1. We are personal. We value knowing and being known by our customers and each other. If you want nameless, faceless service, you should choose another provider. We put "personal" at the front of the list, because it is most important to us; the design we choose will convey this value.

2. Like a hotel concierge, we are professional in attitude, posture, communication and processes.

3. Like a hotel concierge, we solve problems with a can-do attitude and never make excuses.

Our uniforms are khaki pants with pink polo shirts.

Our logo is attached. There are other symbols, not represented in our logo, that may convey our values well, such as a top hat and bow tie, magnifying glass, desk bell, etc.

Please include fields for an individual's name and title, office phone number, mobile phone number, email address and website address (www.marisolsbutlertidying-example.com).

Standard U.S. size: 2" x 3.5"
Updates

I should have mentioned that the purpose of all our advertising - business cards included - is to motivate potential customers to call or email to arrange a free in-home estimate.

```html
<!DOCTYPE html>
<html lang="en">
<head>
<meta charset="utf-8">
<title>Marisol's Butler Tidying – Business Cards</title>
<link rel="stylesheet" href="https://fonts.googleapis.com/css2?family=Open+Sans:wght@400;600;700&display=swap">
<style>
  :root {
    --bg: #e9e6e2;
    --card: #ffffff;
    --pink: #e8378f;
    --ink: #2b2b2b;
    --swoosh-dark: #1f1f1f;
    --swoosh-grey: #8e8e8e;
    --divider: #d6d6d6;
    --figure-a: #f6d3e3;
    --figure-b: #d9a9bf;
    --white: #ffffff;
  }
  * { box-sizing: border-box; margin: 0; padding: 0; }
  html, body { width: 1200px; height: 720px; overflow: hidden; }
  body {
    background: var(--bg);
    font-family: "Open Sans", Arial, sans-serif;
    color: var(--ink);
    position: relative;
  }
  .card {
    position: absolute;
    width: 540px;
    height: 309px;
    background: var(--card);
    box-shadow: 0 2px 10px rgba(0,0,0,0.18);
    overflow: hidden;
  }
  .card--front { left: 45px; top: 205px; }
  .card--back  { left: 615px; top: 205px; }

  .card__waves { position: absolute; inset: 0; width: 100%; height: 100%; }

  .brand {
    position: absolute;
    left: 50px;
    top: 22px;
    width: 130px;
    text-align: center;
  }
  .brand__figure {
    width: 56px;
    height: 78px;
    margin: 0 auto 6px;
    border-radius: 28px 28px 8px 8px;
    background: linear-gradient(180deg, var(--figure-a), var(--figure-b));
  }
  .brand__name {
    font-size: 20px;
    font-weight: 600;
    color: var(--ink);
    line-height: 1;
  }
  .brand__tagline {
    font-size: 9px;
    font-weight: 400;
    color: var(--ink);
    margin-top: 3px;
    letter-spacing: 0.3px;
  }

  .contact {
    position: absolute;
    left: 200px;
    top: 22px;
    padding-left: 14px;
    border-left: 1px solid var(--divider);
  }
  .contact__name { font-size: 16px; font-weight: 700; color: var(--ink); line-height: 1.2; }
  .contact__title { font-size: 11px; font-weight: 600; color: var(--pink); margin-bottom: 4px; }
  .contact__list { list-style: none; }
  .contact__item {
    display: flex;
    align-items: center;
    gap: 7px;
    font-size: 11.5px;
    color: var(--ink);
    line-height: 21px;
    white-space: nowrap;
  }
  .contact__icon { width: 12px; height: 12px; flex: none; }

  .company-band {
    position: absolute;
    right: 24px;
    top: 196px;
    font-size: 13px;
    font-weight: 400;
    color: var(--white);
    white-space: nowrap;
    transform: rotate(-10deg);
    transform-origin: right center;
  }

  .back__figure {
    position: absolute;
    left: 212px;
    top: 45px;
    width: 116px;
    height: 175px;
    border-radius: 50px 50px 14px 14px;
    background: linear-gradient(180deg, var(--figure-a), var(--figure-b));
  }
  .back__web {
    position: absolute;
    left: 0; right: 0;
    top: 245px;
    text-align: center;
    font-size: 15px;
    letter-spacing: 1px;
    color: var(--ink);
  }
</style>
</head>
<body>

<section class="card card--front" aria-label="Business card front">
  <svg class="card__waves" viewBox="0 0 540 309" aria-hidden="true">
    <path d="M0,95 C60,230 260,250 540,135 L540,228 C320,315 120,300 0,225 Z" fill="var(--pink)"/>
    <path d="M0,84 C60,219 260,239 540,124" fill="none" stroke="var(--swoosh-dark)" stroke-width="1.5"/>
    <path d="M0,240 C120,315 320,330 540,243" fill="none" stroke="var(--swoosh-dark)" stroke-width="6"/>
    <path d="M0,256 C120,331 320,346 540,259" fill="none" stroke="var(--swoosh-grey)" stroke-width="7"/>
  </svg>

  <div class="brand">
    <div class="brand__figure" role="img" aria-label="Illustration of a housekeeper mopping the floor"></div>
    <p class="brand__name">Marisol's</p>
    <p class="brand__tagline">Butler Tidying</p>
  </div>

  <div class="contact">
    <p class="contact__name">Your Name</p>
    <p class="contact__title">Title</p>
    <ul class="contact__list">
      <li class="contact__item">
        <svg class="contact__icon" viewBox="0 0 12 12" aria-hidden="true"><circle cx="6" cy="6" r="6" fill="var(--pink)"/><path d="M4,3 L5,3 L5.6,4.6 L4.9,5.2 C5.3,6 6,6.7 6.8,7.1 L7.4,6.4 L9,7 L9,8 C9,8.5 8.5,9 8,9 C5.2,8.8 3.2,6.8 3,4 C3,3.5 3.5,3 4,3 Z" fill="#fff"/></svg>
        012-345-6789
      </li>
      <li class="contact__item">
        <svg class="contact__icon" viewBox="0 0 12 12" aria-hidden="true"><circle cx="6" cy="6" r="6" fill="var(--pink)"/><rect x="4.2" y="2.6" width="3.6" height="6.8" rx="0.6" fill="#fff"/><rect x="4.8" y="3.4" width="2.4" height="4.4" fill="var(--pink)"/></svg>
        012-345-6790
      </li>
      <li class="contact__item">
        <svg class="contact__icon" viewBox="0 0 12 12" aria-hidden="true"><circle cx="6" cy="6" r="6" fill="var(--pink)"/><rect x="3" y="4" width="6" height="4.2" fill="#fff"/><path d="M3,4 L6,6.4 L9,4" fill="none" stroke="var(--pink)" stroke-width="0.7"/></svg>
        info@marisolsbutlertidying-example.com
      </li>
      <li class="contact__item">
        <svg class="contact__icon" viewBox="0 0 12 12" aria-hidden="true"><circle cx="6" cy="6" r="6" fill="var(--pink)"/><circle cx="6" cy="6" r="3" fill="none" stroke="#fff" stroke-width="0.8"/><path d="M3,6 H9 M6,3 C4.8,4.5 4.8,7.5 6,9 M6,3 C7.2,4.5 7.2,7.5 6,9" fill="none" stroke="#fff" stroke-width="0.6"/></svg>
        www.marisolsbutlertidying-example.com
      </li>
    </ul>
  </div>

  <p class="company-band">Marisol's Butler Tidying, LLC</p>
</section>

<section class="card card--back" aria-label="Business card back">
  <div class="back__figure" role="img" aria-label="Illustration of a housekeeper mopping the floor"></div>
  <p class="back__web">www.marisolsbutlertidying-example.com</p>
</section>

</body>
</html>
```